Automotive component supplier needs a business card design

We need a business card design for our company called Vexlo Global Fittings Ltd based in the UK. We are a supplier of interior and exterior components to premium car manufacturers such as Harwick Vale, Denby Stroud, Calloway and Ferrucatti. We would like to see a modern business card design that uses the colour blue.

Target Market(s)

Premium automotive car manufacturers.

Industry/Entity Type

Automotive

Contact Information for Business Card

Company Name : Vexlo Global Fittings Limited
Address: 17 Tamsin Yard, Upper Heath, Warwick, CV32 8LN, United Kingdom
Web Address : www.vexlofittings-demo.co.uk

Font styles to use
Other font styles liked:
• Helvetica

Colors
3176b5
0255a3
85acd3
cfdeed
cee9f5
85cae6
34a6d7
0692cd
9bcb3c

Requirements
Must have
• Clear company logo and a mixture of blue colours.
Nice to have
• A high quality modern image.
Should not have
• Multiple colours.

```html
<!DOCTYPE html>
<html lang="en">
<head>
<meta charset="utf-8">
<title>Vexlo Global Fittings – Business Card</title>
<link rel="stylesheet" href="https://fonts.googleapis.com/css2?family=Source+Sans+3:wght@400;700&display=swap">
<style>
  :root {
    --backdrop: #eef1f4;
    --blue-deep: #0255a3;
    --blue-mid: #3176b5;
    --blue-bright: #0692cd;
    --blue-sky: #34a6d7;
    --blue-pale: #cfdeed;
    --blue-mist: #cee9f5;
    --ink: #0c3f78;
  }
  * { margin: 0; padding: 0; box-sizing: border-box; }
  html, body {
    width: 1200px; height: 900px; overflow: hidden;
    background: var(--backdrop);
  }
  .stage { position: relative; width: 1200px; height: 900px; }
  .card {
    position: absolute;
    width: 556px; height: 342px;
    box-shadow: 0 4px 14px rgba(2, 40, 80, 0.18);
    font-family: "Source Sans 3", "Helvetica Neue", Arial, sans-serif;
  }
  .card--contact {
    left: 238px; top: 62px;
    background: linear-gradient(135deg, var(--blue-mist) 0%, var(--blue-pale) 100%);
    color: var(--ink);
  }
  .card--brand {
    left: 460px; top: 518px; width: 558px;
    background: linear-gradient(135deg, var(--blue-mid) 0%, var(--blue-deep) 100%);
    color: var(--blue-mist);
  }

  .contact {
    position: absolute; left: 0; right: 0; top: 82px;
    text-align: center; font-size: 15.5px; line-height: 20.5px;
  }
  .contact__name { font-weight: 700; font-size: 19.5px; line-height: 22px; color: var(--blue-deep); }
  .contact__role { margin-bottom: 22px; }
  .contact__lines { margin-bottom: 12px; }

  .brand {
    position: absolute; left: 0; right: 0; top: 150px;
    display: flex; align-items: center; justify-content: center; gap: 12px;
  }
  .brand__mark { width: 18px; height: 18px; border-radius: 50%; background: var(--blue-sky); }
  .brand__name {
    font-weight: 700; font-size: 30px; line-height: 34px; letter-spacing: 1.5px;
    text-transform: uppercase; color: var(--blue-mist);
  }
</style>
</head>
<body>
<main class="stage">
  <section class="card card--contact">
    <div class="contact">
      <p class="contact__name">Daniel Reeve</p>
      <p class="contact__role">Director</p>
      <div class="contact__lines">
        <p>1234567890</p>
        <p>1234567890</p>
        <p>info@vexlofittings-demo.co.uk</p>
        <p>www.vexlofittings-demo.co.uk</p>
      </div>
      <p class="contact__address">17 Tamsin Yard, Upper Heath,<br>Warwick, CV32 8LN, United Kingdom</p>
    </div>
  </section>

  <section class="card card--brand">
    <div class="brand">
      <span class="brand__mark"></span>
      <span class="brand__name">Vexlo Global Fittings</span>
    </div>
  </section>
</main>
</body>
</html>
```